Fun relaxed Travel Photography Business Card*

Require a fun, funky and quirky but rememberable business card for a travel photographer

Industry/Entity Type

Photographer

Contact Information for Business Card

Front Card

(my name) Tavo M.

Travel Photographer ( small under travel photographer) “self-proclaimed”

(website logo) wanderingtavo.example

(Instagram logo) @wandering_with_tavo

(Instagram logo) @wandering_with_tavo_2.0 (backup for when Instagram puts Tavo on timeout for bad behaviour)

Tel: N/A (removing the potential awkwardness of me not replying)

Email: (see above)

Back Card

Offending people since 1986

(Bottom right corner) “p.s. travelling made me fatTER”

Font styles to use
Serif

Colors

Designer to choose colors to be used in the design.

Requirements
Must have
• a camera
• a similar cartoon version of me as the "logo" see attached files, try to make as similar as possible

```html
<!DOCTYPE html>
<html lang="en">
<head>
<meta charset="utf-8">
<title>Tavo M. — Travel Photographer Business Cards</title>
<link rel="stylesheet" href="https://fonts.googleapis.com/css2?family=Lato:wght@300;400;700;900&display=swap">
<style>
  :root {
    --stage: #1c1c1e;
    --ink: #151417;
    --paper: #ffffff;
    --muted: #cfcfd2;
    --line: #2a2a2d;
  }
  * { box-sizing: border-box; margin: 0; padding: 0; }
  html, body { width: 1200px; height: 900px; overflow: hidden; }
  body {
    background: var(--stage);
    font-family: "Lato", sans-serif;
    display: flex;
    align-items: center;
    justify-content: center;
    gap: 40px;
  }
  .card {
    position: relative;
    width: 520px;
    height: 300px;
    overflow: hidden;
  }
  .card--back { background: var(--ink); color: var(--paper); }
  .card--front { background: var(--paper); color: var(--ink); }

  .lockup {
    position: absolute;
    display: flex;
    align-items: center;
    gap: 14px;
  }
  .lockup__mark {
    width: 54px; height: 54px;
    border: 3px solid currentColor;
  }
  .lockup__words { display: flex; flex-direction: column; }
  .lockup__name {
    font-size: 50px; font-weight: 400; line-height: 1;
    padding-bottom: 4px;
    border-bottom: 3px solid currentColor;
  }
  .lockup__role {
    font-size: 13px; font-weight: 900; letter-spacing: 0.6px;
    margin-top: 4px;
  }
  .lockup__note {
    font-size: 7px; font-weight: 700; letter-spacing: 0.8px;
  }

  /* back */
  .card--back .lockup { left: 140px; top: 72px; }
  .back__motto {
    position: absolute; left: 128px; top: 178px;
    font-size: 12px; font-weight: 400; letter-spacing: 0.5px;
    color: var(--muted);
  }
  .back__rule {
    position: absolute; left: 0; top: 226px;
    width: 300px; height: 4px; background: var(--paper);
  }
  .back__ps {
    position: absolute; left: 312px; top: 217px;
    font-size: 12px; font-weight: 300; color: var(--muted);
  }
  .back__strip {
    position: absolute; left: 0; bottom: 26px;
    width: 40px; height: 6px; background: var(--paper);
  }

  /* front */
  .card--front .lockup { left: 130px; top: 30px; }
  .contacts {
    position: absolute; left: 0; right: 0; top: 130px;
    display: flex; justify-content: center; gap: 16px;
    font-size: 13px; font-weight: 400; color: #333;
  }
  .contacts__col { display: flex; flex-direction: column; gap: 6px; }
  .contacts__col--social { align-items: flex-end; }
  .contacts__divider { width: 1px; background: var(--ink); }
  .contact { display: flex; align-items: center; gap: 7px; }
  .contact__dot { width: 11px; height: 11px; background: var(--ink); border-radius: 2px; }
  .contact svg { width: 13px; height: 13px; }
  .front__band {
    position: absolute; left: 0; right: 0; top: 222px; height: 34px;
    background: var(--ink); color: var(--paper);
    display: flex; align-items: center; justify-content: center;
    font-size: 17px; font-weight: 700; letter-spacing: 2.5px;
  }
</style>
</head>
<body>
  <section class="card card--back" aria-label="Card back">
    <div class="lockup">
      <div class="lockup__mark"></div>
      <div class="lockup__words">
        <span class="lockup__name">Tavo M.</span>
        <span class="lockup__role">TRAVEL PHOTOGRAPHER</span>
        <span class="lockup__note">SELF-PROCLAIMED</span>
      </div>
    </div>
    <p class="back__motto">OFFENDING PEOPLE SINCE 1986</p>
    <div class="back__rule"></div>
    <p class="back__ps">p.s. travelling made me fatter</p>
    <div class="back__strip"></div>
  </section>

  <section class="card card--front" aria-label="Card front">
    <div class="lockup">
      <div class="lockup__mark"></div>
      <div class="lockup__words">
        <span class="lockup__name">Tavo M.</span>
        <span class="lockup__role">TRAVEL PHOTOGRAPHER</span>
        <span class="lockup__note">SELF-PROCLAIMED</span>
      </div>
    </div>
    <div class="contacts">
      <div class="contacts__col contacts__col--social">
        <span class="contact">@wandering_with_tavo <span class="contact__dot"></span></span>
        <span class="contact">@wandering_with_tavo_2.0 <span class="contact__dot"></span></span>
      </div>
      <div class="contacts__divider"></div>
      <div class="contacts__col">
        <span class="contact">
          <svg viewBox="0 0 16 16" aria-hidden="true"><path d="M3 2h3l1 3-2 1a9 9 0 0 0 5 5l1-2 3 1v3c0 1-1 1-1 1A12 12 0 0 1 2 3s0-1 1-1z" fill="#151417"/></svg>
          555 0142 7788
        </span>
        <span class="contact">
          <svg viewBox="0 0 16 16" aria-hidden="true"><rect x="1.5" y="3.5" width="13" height="9" fill="none" stroke="#151417" stroke-width="1.5"/><path d="M1.5 3.5 8 9l6.5-5.5" fill="none" stroke="#151417" stroke-width="1.5"/></svg>
          info@wanderingtavo.example
        </span>
      </div>
    </div>
    <div class="front__band">www.wanderingtavo.example</div>
  </section>
</body>
</html>
```